Business card for Chicago based Private Equity Company

We need a business card for our PE company called Crestline Holdings. We want a simple and clean, yet creative card design. The back side should reflect our logo. Also would like to see embossed ideas. Should reflect strength and growth. Our logo is attached. Also need editable file. Details are as follows for Business Card:

Dana Welmore Co-Founder 2750 Marlow Avenue Suite 410 Fernvale, IL 60914 http://www.crestlineholdingsllc.example (D) 630.555.0147 (C) 312.555.0182 (E) dw@crestlineholdingsllc.example

```html
<!DOCTYPE html>
<html lang="en">
<head>
<meta charset="utf-8">
<title>Crestline Holdings – Business Card</title>
<link href="https://fonts.googleapis.com/css2?family=Didact+Gothic&display=swap" rel="stylesheet">
<style>
  :root {
    --page-bg: #e6e7e9;
    --card-bg: #fbfbfb;
    --ink: #2b2b2b;
    --ink-soft: #4a4a4a;
    --brand-blue: #1f86d6;
    --brand-blue-light: #3aa0ea;
    --band-edge: #1c1c1c;
    --white: #ffffff;
  }
  html, body {
    margin: 0;
    width: 1200px;
    height: 900px;
    overflow: hidden;
    background: var(--page-bg);
    font-family: "Didact Gothic", "Century Gothic", sans-serif;
  }
  .card {
    position: absolute;
    left: 75px;
    top: 150px;
    width: 1050px;
    height: 600px;
    background: var(--card-bg);
    overflow: hidden;
    box-shadow: 0 10px 30px rgba(0,0,0,0.12);
  }
  .brand {
    position: absolute;
    left: 0;
    right: 0;
    top: 110px;
    display: flex;
    justify-content: center;
    align-items: center;
    gap: 22px;
  }
  .brand-dot {
    width: 92px;
    height: 92px;
    border-radius: 50%;
    background: var(--brand-blue);
  }
  .brand-name {
    color: var(--ink);
    font-size: 42px;
    letter-spacing: 4px;
    text-transform: uppercase;
    line-height: 1;
    border-bottom: 1.5px solid var(--ink);
    padding-bottom: 8px;
  }
  .identity {
    position: absolute;
    left: 0;
    right: 0;
    top: 290px;
    text-align: center;
    font-size: 22px;
    font-variant: small-caps;
    letter-spacing: 2px;
    color: var(--ink);
  }
  .identity .divider {
    display: inline-block;
    width: 1.5px;
    height: 24px;
    background: var(--ink);
    margin: 0 14px;
    vertical-align: -4px;
  }
  .identity .role { color: var(--ink-soft); }
  .contact {
    position: absolute;
    left: 60px;
    top: 392px;
    font-size: 14px;
    font-variant: small-caps;
    letter-spacing: 1.2px;
    color: var(--ink-soft);
  }
  .contact-line { margin-bottom: 12px; white-space: nowrap; }
  .icon {
    display: inline-block;
    width: 10px;
    height: 10px;
    border-radius: 50%;
    background: var(--ink);
    margin: 0 6px 0 12px;
    vertical-align: -1px;
  }
  .contact-line .icon:first-child { margin-left: 0; }
  .band {
    position: absolute;
    left: 0;
    top: 0;
    width: 1050px;
    height: 600px;
  }
  .band-url {
    fill: var(--white);
    font-family: "Didact Gothic", "Century Gothic", sans-serif;
    font-size: 19px;
    font-variant: small-caps;
    letter-spacing: 3px;
  }
</style>
</head>
<body>
  <div class="card">
    <svg class="band" viewBox="0 0 1050 600" aria-hidden="true">
      <defs>
        <linearGradient id="bandFill" x1="0" y1="1" x2="1" y2="0">
          <stop offset="0" stop-color="#1f86d6"/>
          <stop offset="1" stop-color="#3aa0ea"/>
        </linearGradient>
      </defs>
      <path d="M 0 600 Q 500 600 1050 430 L 1050 600 Z" fill="url(#bandFill)"/>
      <path d="M 0 600 Q 500 600 1050 430" fill="none" stroke="#1c1c1c" stroke-width="4"/>
      <text class="band-url" x="720" y="568" text-anchor="middle" transform="rotate(-12 720 568)">www.crestlineholdingsllc.example</text>
    </svg>

    <div class="brand">
      <div class="brand-dot"></div>
      <div class="brand-name">Crestline Holdings</div>
    </div>

    <div class="identity">
      <span class="name">Dana Welmore</span><span class="divider"></span><span class="role">Co-Founder</span>
    </div>

    <div class="contact">
      <div class="contact-line"><span class="icon"></span>2750 Marlow Avenue Suite 410, Fernvale, IL 60914<span class="icon"></span>www.crestlineholdingsllc.example<span class="icon"></span>dw@crestlineholdingsllc.example</div>
      <div class="contact-line"><span class="icon"></span>630.555.0147<span class="icon"></span>312.555.0182<span class="icon"></span>630.555.0148</div>
    </div>
  </div>
</body>
</html>
```